New Web 2.0 responsive website for popup advertisement network

We need a responsive web design for a new popup advertisement network company Clickverra.com based in Newport Beach, California.

We need the design for the main site as well as the interface design for the member portal login area.

Below is the requirement and concept for the website / portal. 

1. With reference to http://tabvexora.com/  (Overall  home layout design and menu bar can follow this website (except the homepage banner section) ,color theme change to #81D8D0)

2. Integrate 3 step process in the homepage for easy reference. Follow the concept in the website below but use better graphic and images to present. Can integrate this in homepage banner section.
   reference:  http://glimrack.net/, http://zentablo.com/ 

3.  Use the nice look ad tag line in the homepage banner section as well. Can refer to the site below.
     http://www.yieldmorva.com/#publishers
 
4. Sign up button must be clear and obvious in the homepage.

We required the design for the pages below.
1. Homepage
2. Dashboard
3. Add Website
3. Code Generator
4. Website
5. Report

(Please refer to the attached image for the concept and field required in the page)

Target Market(s)

US, web owner such as blogger or content sites

Industry/Entity Type

Advertising

Logo Text

Scientific and Fun

Coding

Coded - Design and coding required

Number of Pages Required

5+ page

Font styles to use
Sans Serif

Colors
0692cd

```html
<!DOCTYPE html>
<html lang="en">
<head>
<meta charset="utf-8">
<title>Clickverra – Pop-Under Advertising Network</title>
<link href="https://fonts.googleapis.com/css2?family=Open+Sans:wght@300;400;600;700;800&display=swap" rel="stylesheet">
<style>
:root{
  --teal:#81d8d0;
  --blue:#0692cd;
  --blue-light:#1fa8e6;
  --ink:#333333;
  --muted:#555555;
  --band:#444444;
  --footer:#454545;
  --footer-base:#3a3a3a;
  --soft:#f4f4f4;
  --white:#ffffff;
}
*{margin:0;padding:0;box-sizing:border-box}
html,body{width:1200px;height:2817px;overflow:hidden}
body{font-family:"Open Sans",Arial,sans-serif;color:var(--ink);background:var(--white);position:relative}
.abs{position:absolute}

/* header */
.site-header{position:absolute;left:0;top:0;width:1200px;height:98px;background:var(--white)}
.brand{position:absolute;left:98px;top:30px;display:flex;align-items:center;gap:14px}
.brand-mark{width:34px;height:34px;border-radius:50%;background:#4a4a4a}
.brand-name{font-size:26px;font-weight:700;color:#4a4a4a;letter-spacing:1px}
.main-nav{position:absolute;top:42px;left:0;width:1200px;font-size:15px;color:#666}
.main-nav span{position:absolute;top:0}
.main-nav .active{color:var(--blue)}
.main-nav .active::after{content:"";position:absolute;left:-14px;right:-14px;top:54px;height:3px;background:var(--blue)}

/* hero */
.hero{position:absolute;left:0;top:98px;width:1200px;height:559px;background:var(--teal);overflow:hidden}
.step-label{position:absolute;top:163px;width:200px;text-align:center;font-size:15px;font-weight:700;color:var(--white);letter-spacing:.5px}
.hero-title{position:absolute;top:212px;left:0;width:1200px;text-align:center;font-size:62px;line-height:96px;font-weight:800;color:var(--white);letter-spacing:1px;z-index:2}
.hero-art{position:absolute;left:50px;top:250px;width:1100px;height:309px;background:linear-gradient(180deg,rgba(74,74,74,0) 0%,rgba(74,74,74,.25) 45%,rgba(60,60,60,.85) 100%);border-radius:40px 40px 0 0;z-index:1}
.slider-arrow{position:absolute;top:212px;width:47px;height:50px;background:#2f4a47;z-index:3}

/* cta band */
.cta-band{position:absolute;left:0;top:657px;width:1200px;height:132px;background:var(--band)}
.cta-title{position:absolute;left:98px;top:40px;font-size:26px;font-weight:700;color:var(--white)}
.cta-text{position:absolute;left:98px;top:80px;font-size:12px;color:#bbbbbb}
.btn-signup{position:absolute;left:665px;top:28px;width:334px;height:79px;background:linear-gradient(180deg,var(--blue-light),var(--blue));border-radius:3px;color:var(--white);font-size:21px;font-weight:600;text-align:center;line-height:79px}

/* welcome */
.section-title{position:absolute;left:0;width:1200px;text-align:center;font-size:31px;font-weight:700;color:var(--ink)}
.welcome-note{position:absolute;left:100px;top:902px;width:1000px;text-align:center;font-size:12.5px;line-height:21px;color:var(--muted)}
.audience{position:absolute;top:980px;width:500px;text-align:center}
.audience-art{margin:0 auto;width:120px;height:120px;border-radius:10px}
.audience h3{margin-top:30px;font-size:24px;font-weight:600;color:var(--blue)}
.audience p{margin:14px auto 0;width:490px;font-size:12px;line-height:21px;color:var(--muted)}
.btn-more{display:inline-block;margin-top:20px;width:122px;height:54px;line-height:54px;background:linear-gradient(180deg,var(--blue-light),var(--blue));color:var(--white);font-size:14px;border-radius:3px}

/* features */
.features{position:absolute;left:0;top:1356px;width:1200px;height:546px;background:var(--soft)}
.feature{position:absolute;width:330px}
.feature-icon{position:absolute;left:0;top:0;width:90px;height:90px;border-radius:50%;background:linear-gradient(180deg,var(--blue-light),var(--blue))}
.feature h4{position:absolute;left:103px;top:10px;width:240px;font-size:21px;font-weight:400;line-height:26px;color:var(--blue)}
.feature p{position:absolute;left:103px;top:66px;width:215px;font-size:12.5px;line-height:16px;color:var(--muted)}

/* insights */
.stat{position:absolute;top:2058px;width:260px;text-align:center}
.stat svg{display:block;margin:0 auto}
.stat-value{margin-top:48px;font-size:31px;color:var(--ink)}
.stat-label{margin-top:6px;font-size:20px;color:var(--ink)}

/* footer */
.site-footer{position:absolute;left:0;top:2404px;width:1200px;height:329px;background:var(--footer);color:#dddddd}
.footer-brand{position:absolute;left:98px;top:66px;display:flex;align-items:center;gap:14px}
.footer-brand .brand-mark{background:#8a8a8a}
.footer-brand .brand-name{color:#9a9a9a}
.footer-about{position:absolute;left:98px;top:128px;width:300px;font-size:12px;line-height:21px;color:#e6e6e6}
.footer-head{position:absolute;top:70px;font-size:20px;font-weight:600;color:#bdbdbd}
.footer-links{position:absolute;top:122px;font-size:12px;line-height:21px;color:#e6e6e6}
.newsletter-text{position:absolute;left:659px;top:120px;width:240px;font-size:12px;line-height:22px;color:#e6e6e6}
.newsletter-input{position:absolute;left:655px;top:188px;width:231px;height:52px;background:var(--white);color:#555;font-size:12px;line-height:52px;padding-left:14px}
.newsletter-submit{position:absolute;left:655px;top:263px;width:70px;height:33px;background:var(--blue);color:var(--white);font-size:12px;line-height:33px;text-align:center;border-radius:2px}
.social-item{position:absolute;left:1018px;font-size:12px;color:#e6e6e6;display:flex;align-items:center;gap:10px}
.social-dot{width:16px;height:16px;background:#8a8a8a}
.copyright{position:absolute;left:0;top:2733px;width:1200px;height:84px;background:var(--footer-base);color:#cccccc;text-align:center;font-size:12px;line-height:84px}
</style>
</head>
<body>

<header class="site-header">
  <div class="brand"><div class="brand-mark"></div><div class="brand-name">CLICKVERRA</div></div>
  <nav class="main-nav">
    <span class="active" style="left:577px">HOME</span>
    <span style="left:668px">ADVERTISER</span>
    <span style="left:804px">PUBLISHER</span>
    <span style="left:932px">CONTACT</span>
    <span style="left:1048px">ABOUT</span>
  </nav>
</header>

<section class="hero">
  <svg class="abs" style="left:0;top:0" width="1200" height="200" viewBox="0 0 1200 200">
    <circle cx="370" cy="90" r="53" fill="#ffffff"/>
    <circle cx="601" cy="90" r="53" fill="#ffffff"/>
    <circle cx="830" cy="90" r="53" fill="#ffffff"/>
    <path d="M430 120 Q480 150 530 95" fill="none" stroke="#ffffff" stroke-width="4"/>
    <path d="M518 96 L532 92 L530 108" fill="none" stroke="#ffffff" stroke-width="4"/>
    <path d="M662 95 Q715 60 765 110" fill="none" stroke="#ffffff" stroke-width="4"/>
    <path d="M752 110 L767 113 L767 98" fill="none" stroke="#ffffff" stroke-width="4"/>
  </svg>
  <div role="img" aria-label="Sign up form icon" class="abs" style="left:340px;top:60px;width:60px;height:60px;border-radius:8px;background:linear-gradient(135deg,#dfe9f3,#f4b860)"></div>
  <div role="img" aria-label="Megaphone icon" class="abs" style="left:571px;top:60px;width:60px;height:60px;border-radius:50%;background:linear-gradient(135deg,#f5c542,#555555)"></div>
  <div role="img" aria-label="Stack of gold coins icon" class="abs" style="left:800px;top:60px;width:60px;height:60px;border-radius:8px;background:linear-gradient(180deg,#f7d34a,#d9a514)"></div>
  <div class="step-label" style="left:270px">SIGN UP</div>
  <div class="step-label" style="left:501px">SHOW RELEVANT ADS</div>
  <div class="step-label" style="left:730px">EARN MONEY</div>
  <div class="hero-title">WE MAKE ADVERTISING<br>BEAUTIFUL</div>
  <div class="hero-art" role="img" aria-label="Illustration of suited arms holding a phone, laptop, megaphone, calculator and report"></div>
  <div class="slider-arrow" style="left:0">
    <svg width="47" height="50" viewBox="0 0 47 50"><path d="M27 17 L19 25 L27 33" fill="none" stroke="#fff" stroke-width="2.5"/></svg>
  </div>
  <div class="slider-arrow" style="left:1153px">
    <svg width="47" height="50" viewBox="0 0 47 50"><path d="M20 17 L28 25 L20 33" fill="none" stroke="#fff" stroke-width="2.5"/></svg>
  </div>
</section>

<section class="cta-band">
  <div class="cta-title">DO YOU HAVE A WEBSITE?</div>
  <div class="cta-text">Tabvexora will maximize your advertising revenue with cutting-edge pop-under technology.</div>
  <div class="btn-signup">SIGN UP FOR AN ACCOUNT</div>
</section>

<section class="welcome">
  <h2 class="section-title" style="top:843px">WELCOME TO CLICKVERRA</h2>
  <p class="welcome-note">We use cookies and similar technologies on our web site to improve performance and make your experience better. Your use of our web site indicates your consent to the usage of cookies as previously mentioned.</p>
  <div class="audience" style="left:85px">
    <div class="audience-art" role="img" aria-label="Presentation easel icon" style="background:linear-gradient(180deg,#5aaed8,#d9823a)"></div>
    <h3>ADVERTISERS</h3>
    <p>Premium traffic, premium publishers, dozens of targeting options and advanced real-time reports will insure your way to success.</p>
    <span class="btn-more">Read More</span>
  </div>
  <div class="audience" style="left:612px">
    <div class="audience-art" role="img" aria-label="Code window with gear icon" style="background:linear-gradient(180deg,#4a4a4a,#e8e8e8)"></div>
    <h3>PUBLISHERS</h3>
    <p>Premium traffic, premium publishers, dozens of targeting options and advanced real-time reports will insure your way to success.</p>
    <span class="btn-more">Read More</span>
  </div>
</section>

<section class="features">
  <h2 class="section-title" style="top:65px">POP-UNDER SERVICE FEATURES</h2>

  <div class="feature" style="left:100px;top:153px">
    <div class="feature-icon"><svg width="90" height="90" viewBox="0 0 90 90"><circle cx="45" cy="45" r="13" fill="none" stroke="#fff" stroke-width="3"/><path d="M45 37 V45 H51" fill="none" stroke="#fff" stroke-width="3"/></svg></div>
    <h4>REALTIME BIDDING<br>SYSTEM</h4>
    <p>Our advanced algorhytms will display the highest paying / top converting campaign.</p>
  </div>
  <div class="feature" style="left:438px;top:153px">
    <div class="feature-icon"><svg width="90" height="90" viewBox="0 0 90 90"><circle cx="45" cy="38" r="7" fill="#fff"/><path d="M32 57 Q32 46 45 46 Q58 46 58 57 Z" fill="#fff"/></svg></div>
    <h4>DEDICATED ACCOUNT<br>MANAGER</h4>
    <p>Our advanced algorhytms will display the highest paying / top converting campaign.</p>
  </div>
  <div class="feature" style="left:786px;top:153px">
    <div class="feature-icon"><svg width="90" height="90" viewBox="0 0 90 90"><ellipse cx="41" cy="42" rx="12" ry="9" fill="#fff"/><path d="M33 48 L30 56 L39 50 Z" fill="#fff"/><ellipse cx="52" cy="50" rx="10" ry="7" fill="#fff" stroke="#0692cd" stroke-width="2"/></svg></div>
    <h4>24/7 CUSTOMER<br>SUPPORT</h4>
    <p>Our advanced algorhytms will display the highest paying / top converting campaign.</p>
  </div>
  <div class="feature" style="left:100px;top:335px">
    <div class="feature-icon"><svg width="90" height="90" viewBox="0 0 90 90"><path d="M32 32 V57 H58" fill="none" stroke="#fff" stroke-width="2.5"/><rect x="37" y="45" width="4" height="10" fill="#fff"/><rect x="43" y="39" width="4" height="16" fill="#fff"/><rect x="49" y="42" width="4" height="13" fill="#fff"/></svg></div>
    <h4>REALTIME<br>REPORTS</h4>
    <p>Our advanced algorhytms will display the highest paying / top converting campaign.</p>
  </div>
  <div class="feature" style="left:438px;top:335px">
    <div class="feature-icon"><svg width="90" height="90" viewBox="0 0 90 90"><rect x="29" y="35" width="32" height="20" fill="none" stroke="#fff" stroke-width="3"/><circle cx="45" cy="45" r="5" fill="#fff"/></svg></div>
    <h4>INSTANT DEPOSITS /<br>WITHDRAWS</h4>
    <p>Our advanced algorhytms will display the highest paying / top converting campaign.</p>
  </div>
  <div class="feature" style="left:786px;top:335px">
    <div class="feature-icon"><svg width="90" height="90" viewBox="0 0 90 90"><circle cx="45" cy="45" r="11" fill="none" stroke="#fff" stroke-width="6" stroke-dasharray="5 3"/><circle cx="45" cy="45" r="7" fill="#fff"/><circle cx="45" cy="45" r="3.5" fill="#0692cd"/></svg></div>
    <h4>FULL<br>CONTROL</h4>
    <p>Our advanced algorhytms will display the highest paying / top converting campaign.</p>
  </div>
</section>

<section class="insights">
  <h2 class="section-title" style="top:1962px">NETWORK INSIGHTS</h2>
  <div class="stat" style="left:48px">
    <svg width="160" height="160" viewBox="0 0 160 160"><circle cx="80" cy="80" r="76" fill="none" stroke="#333" stroke-width="7"/><rect x="48" y="56" width="64" height="48" fill="none" stroke="#333" stroke-width="5"/><rect x="58" y="68" width="20" height="16" fill="#333"/><rect x="84" y="68" width="18" height="4" fill="#333"/><rect x="84" y="78" width="18" height="4" fill="#333"/><rect x="58" y="90" width="44" height="4" fill="#333"/></svg>
    <div class="stat-value">213</div><div class="stat-label">WEBSITES</div>
  </div>
  <div class="stat" style="left:323px">
    <svg width="160" height="160" viewBox="0 0 160 160"><circle cx="80" cy="80" r="76" fill="none" stroke="#333" stroke-width="7"/><path d="M55 62 H72 A8 8 0 1 1 88 62 H102 V78 A8 8 0 1 1 102 94 V106 H55 Z" fill="#333"/></svg>
    <div class="stat-value">21</div><div class="stat-label">AD CAMPAIGNS</div>
  </div>
  <div class="stat" style="left:593px">
    <svg width="160" height="160" viewBox="0 0 160 160"><circle cx="80" cy="80" r="76" fill="none" stroke="#333" stroke-width="7"/><g fill="none" stroke="#333" stroke-width="5" stroke-linejoin="round"><path d="M80 52 L94 59 L80 66 L66 59 Z M66 59 V73 L80 80 L94 73 V59 M80 66 V80"/><path d="M64 80 L78 87 L64 94 L50 87 Z M50 87 V101 L64 108 L78 101 V87 M64 94 V108"/><path d="M96 80 L110 87 L96 94 L82 87 Z M82 87 V101 L96 108 L110 101 V87 M96 94 V108"/></g></svg>
    <div class="stat-value">0</div><div class="stat-label">POP-UNDERS TODAY</div>
  </div>
  <div class="stat" style="left:880px">
    <svg width="160" height="160" viewBox="0 0 160 160"><circle cx="80" cy="80" r="76" fill="none" stroke="#333" stroke-width="7"/><text x="80" y="100" text-anchor="middle" font-family="Open Sans, Arial, sans-serif" font-size="56" font-weight="700" fill="#333">$</text></svg>
    <div class="stat-value">$9.00</div><div class="stat-label">TOP NETWORK BID</div>
  </div>
</section>

<footer class="site-footer">
  <div class="footer-brand"><div class="brand-mark"></div><div class="brand-name">CLICKVERRA</div></div>
  <p class="footer-about">Neque porro quisquam est qui dolorem ipsum quia dolor sit amet, consectetur, adipisci velit..<br><br>At vero eos et accusamus et iusto odio dignissimos ducimus qui blanditiis praesentium voluptatum deleniti atque corrupti quos dolores</p>
  <div class="footer-head" style="left:471px">LEGAL</div>
  <div class="footer-links" style="left:471px">Terms of Service<br>Privacy Policy<br>Regulation</div>
  <div class="footer-head" style="left:659px">NEWSLETTER</div>
  <p class="newsletter-text">Do you want to get email updates from a website or blog</p>
  <div class="newsletter-input">Enter Your Mail Id</div>
  <div class="newsletter-submit">Submit</div>
  <div class="footer-head" style="left:1018px">SOCIAL</div>
  <div class="social-item" style="top:125px"><span class="social-dot"></span>Friendloop</div>
  <div class="social-item" style="top:157px"><span class="social-dot"></span>Chirpline</div>
  <div class="social-item" style="top:189px"><span class="social-dot"></span>RSS</div>
</footer>
<div class="copyright">©2015 clickverra.com. All rights reserved.</div>

</body>
</html>
```